Postcard Design

I am a merchandiser for a jewelry company called marla + juniper. The jewelry style is chic with vintage inspiration. My boutique link is www.marlaandjuniper.com/boutique/dianevolkert. This is a great example to use when designing the postcard. I mainly advertise my boutique link for people to shop online for convenience. The other side is that outside of advertising my boutique link I host "pop-up shops" where a customer can host a party and earn up to $250 in free jewelry depending on how much is sold at the party. I would like my postcard to target Brides and bridemaids as I am using the postcards for a wedding fair event on January 18th. I would like to include a hook on the postcard to draw in brides/bridesmaids to be a hostess in order to earn the free jewelry credit as bridesmaids' gifts and/or bridal wear.
Updates

Payment has been guaranteed and I have added the company's logo.

Example of hostess wanted language: "Hostesses wanted! Host a pop-up in January and receive TWO retro glam pieces + $250 free jewelry credit to spend on bridesmaids' gifts and/or bridal jewelry!"

```html
<!DOCTYPE html>
<html lang="en">
<head>
<meta charset="utf-8">
<title>marla + juniper — Hostess Postcard</title>
<link href="https://fonts.googleapis.com/css2?family=Playfair+Display:wght@400&display=swap" rel="stylesheet">
<style>
  :root {
    --sky-light: #f4f3e9;
    --sky-mint: #e2eee6;
    --blossom: #eab8c2;
    --blossom-deep: #d98a9c;
    --gold-light: #e6c67a;
    --gold: #b8893a;
    --gold-dark: #6e4c1e;
    --ink: #2b2826;
    --photo-warm: #8a6f66;
    --photo-dark: #4a3a33;
    --photo-skin: #d9b3a4;
  }
  * { margin: 0; padding: 0; box-sizing: border-box; }
  html, body { width: 1200px; height: 912px; overflow: hidden; }
  body { font-family: "Playfair Display", Georgia, serif; color: var(--ink); }

  .postcard {
    position: relative;
    width: 1200px;
    height: 912px;
    overflow: hidden;
    background: var(--sky-light);
  }

  .blossom-backdrop {
    position: absolute;
    inset: 0;
    background:
      radial-gradient(ellipse 420px 360px at 120px 620px, var(--blossom) 0%, transparent 70%),
      radial-gradient(ellipse 380px 300px at 520px 300px, rgba(234,184,194,0.7) 0%, transparent 70%),
      radial-gradient(ellipse 300px 240px at 1080px 520px, rgba(234,184,194,0.6) 0%, transparent 70%),
      radial-gradient(ellipse 300px 260px at 40px 180px, rgba(217,138,156,0.55) 0%, transparent 70%),
      linear-gradient(160deg, var(--sky-mint) 0%, var(--sky-light) 55%, #f6efe6 100%);
  }

  .gallery-frame {
    position: absolute;
    padding: 22px;
    background: linear-gradient(135deg, var(--gold-light) 0%, var(--gold) 40%, var(--gold-dark) 70%, var(--gold) 100%);
    box-shadow: 0 4px 10px rgba(60, 40, 20, 0.35);
  }
  .gallery-frame::before {
    content: "";
    position: absolute;
    inset: 14px;
    border: 3px solid var(--gold-light);
    opacity: 0.8;
  }
  .frame-photo { position: relative; width: 100%; height: 100%; }

  .frame-necklace { left: 66px; top: 57px; width: 245px; height: 330px; transform: rotate(-8deg); }
  .frame-necklace .frame-photo { background: linear-gradient(160deg, #c57b6c 0%, var(--photo-warm) 35%, #cfc8c4 60%, var(--photo-dark) 100%); }

  .frame-headpiece { left: 474px; top: 43px; width: 256px; height: 268px; }
  .frame-headpiece .frame-photo { background: linear-gradient(180deg, #3b2c25 0%, var(--photo-dark) 60%, #a89a8a 100%); }

  .frame-statement { left: 861px; top: 57px; width: 262px; height: 330px; transform: rotate(8deg); }
  .frame-statement .frame-photo { background: linear-gradient(150deg, var(--photo-skin) 0%, #a88470 45%, #c9c4c6 70%, var(--photo-warm) 100%); }

  .headline {
    position: absolute;
    left: 0; right: 0;
    top: 440px;
    text-align: center;
    font-size: 50px;
    line-height: 60px;
    font-weight: 400;
  }
  .subline {
    position: absolute;
    left: 0; right: 0;
    top: 695px;
    text-align: center;
    font-size: 31px;
    line-height: 40px;
  }
  .footnote {
    position: absolute;
    right: 18px;
    bottom: 12px;
    font-size: 17px;
  }
</style>
</head>
<body>
  <main class="postcard">
    <div class="blossom-backdrop" role="img" aria-label="Soft pastel sky with pink cherry blossom branches"></div>

    <figure class="gallery-frame frame-necklace">
      <div class="frame-photo" role="img" aria-label="Crystal statement necklace displayed beside a pink flower"></div>
    </figure>
    <figure class="gallery-frame frame-headpiece">
      <div class="frame-photo" role="img" aria-label="Jeweled chain headpiece worn in dark hair"></div>
    </figure>
    <figure class="gallery-frame frame-statement">
      <div class="frame-photo" role="img" aria-label="Woman wearing a silver crystal statement necklace"></div>
    </figure>

    <h1 class="headline">By hosting a party, you<br>can earn up to $250 in<br>FREE JEWLERY*!</h1>
    <p class="subline">That’s $250 you could spend on other expenses,<br>like a day at the spa on your honeymoon!</p>
    <p class="footnote">*amount depends on amount sold at party</p>
  </main>
</body>
</html>
```